Celebrating 10 Years

advertisement for print magazine
also to be used on email.
Updates

The relevant information I need (beside my photo and the firm logo) is:
my name: Tom Harlowe
Circuit Civil Mediator
the 800 telephone number provided
reference to the 10 years (new design)
and the words:
Thank You.

Target Market(s)

clients

Industry/Entity Type

Mediation Legal

Font styles to use
Sans Serif

Colors
0054AA
0677BA
7BADD7
CADEEF
E8F1F8
FFF300
FFF600
FEFA6F
FFFEC7
FFFEE8

```html
<!DOCTYPE html>
<html lang="en">
<head>
<meta charset="utf-8">
<title>Tom Harlowe Esq. – Celebrating 10 Years</title>
<link rel="stylesheet" href="https://fonts.googleapis.com/css2?family=Outfit:wght@400;500;600;700;800&display=swap">
<style>
  :root {
    --bg-top: #1a1448;
    --bg-bottom: #21103a;
    --gold: #e9a922;
    --gold-soft: #d9a53c;
    --sign-blue: #0677ba;
    --string-blue: #0677ba;
    --ink-navy: #1a1450;
    --white: #ffffff;
    --muted: #e3e0ee;
  }
  * { margin: 0; padding: 0; box-sizing: border-box; }
  html, body { width: 848px; height: 1200px; overflow: hidden; background: var(--bg-bottom); }
  body { font-family: "Outfit", sans-serif; }

  .ad {
    position: relative;
    width: 848px;
    height: 1200px;
    overflow: hidden;
    background: linear-gradient(180deg, var(--bg-top) 0%, #1c1345 55%, var(--bg-bottom) 100%);
  }

  .portrait {
    position: absolute;
    left: 0;
    top: 20px;
    width: 540px;
    height: 880px;
    border-radius: 260px 260px 0 0;
    background: linear-gradient(180deg, #8f8470 0%, #b89a86 22%, #a8877a 42%, #3a3f6e 62%, #232657 82%, rgba(30,20,70,0) 100%);
    opacity: 0.85;
  }

  .brand {
    position: absolute;
    left: 500px;
    top: 70px;
    width: 320px;
    text-align: center;
  }
  .brand-dot {
    width: 120px;
    height: 120px;
    margin: 0 auto 22px;
    border-radius: 50%;
    background: var(--gold);
  }
  .brand-name {
    color: var(--white);
    font-weight: 500;
    font-size: 30px;
    line-height: 1.15;
    letter-spacing: 0.04em;
  }

  .sign { position: absolute; left: 400px; top: 400px; width: 430px; height: 420px; }

  .headline {
    position: absolute;
    left: 0;
    width: 848px;
    text-align: center;
  }
  .name {
    top: 816px;
    color: var(--gold);
    font-weight: 700;
    font-size: 78px;
    line-height: 1;
    letter-spacing: -0.01em;
  }
  .role {
    top: 906px;
    color: var(--gold-soft);
    font-weight: 700;
    font-size: 37px;
    letter-spacing: 0.2em;
  }
  .cert {
    top: 956px;
    color: var(--gold-soft);
    font-weight: 500;
    font-size: 25px;
  }
  .contact-title {
    top: 1038px;
    color: var(--muted);
    font-weight: 600;
    font-size: 24px;
    letter-spacing: 0.2em;
  }
  .contact-line {
    color: var(--muted);
    font-weight: 400;
    font-size: 24px;
  }
  .contact-line.phones { top: 1100px; }
  .contact-line.emails { top: 1133px; }
  .sep { margin: 0 14px; }
</style>
</head>
<body>
<main class="ad">
  <div class="portrait" role="img" aria-label="Portrait photo of Tom Harlowe in a navy suit and striped tie"></div>

  <div class="brand">
    <div class="brand-dot"></div>
    <div class="brand-name">Crestview<br>Mediation Group</div>
  </div>

  <svg class="sign" viewBox="400 400 430 420" aria-label="Thank You – Celebrating 10 Years">
    <line x1="637" y1="423" x2="547" y2="530" stroke="var(--string-blue)" stroke-width="2"/>
    <line x1="637" y1="423" x2="694" y2="548" stroke="var(--string-blue)" stroke-width="2"/>
    <circle cx="637" cy="423" r="8" fill="#f2f2f2"/>
    <g transform="rotate(4 610 655)">
      <rect x="430" y="530" width="365" height="250" fill="var(--sign-blue)"/>
      <circle cx="508" cy="568" r="6" fill="var(--ink-navy)"/>
      <circle cx="722" cy="568" r="6" fill="var(--ink-navy)"/>
      <text x="612" y="652" text-anchor="middle" font-family="Outfit, sans-serif" font-weight="800" font-size="56" fill="var(--ink-navy)">THANK YOU</text>
      <text x="612" y="686" text-anchor="middle" font-family="Outfit, sans-serif" font-weight="700" font-size="22" letter-spacing="4" fill="var(--white)">CELEBRATING</text>
      <text x="612" y="740" text-anchor="middle" font-family="Outfit, sans-serif" font-weight="800" font-size="52" fill="var(--ink-navy)">10 YEARS</text>
    </g>
  </svg>

  <h1 class="headline name">TOM HARLOWE Esq.</h1>
  <p class="headline role">CIVIL CIRCUIT MEDIATOR</p>
  <p class="headline cert">CERTIFIED BY SUPREME COURT OF FLORIDA</p>

  <p class="headline contact-title">CONTACT INFORMATION</p>
  <p class="headline contact-line phones">Toll Free: (800) 555-0142<span class="sep">|</span>Mobile: (555) 318 2296</p>
  <p class="headline contact-line emails">THarlowe@crestview-adr.com<span class="sep">|</span>TomHarlowe@mailbox.com</p>
</main>
</body>
</html>
```